Tallowfern Letterheads Design

Hello, we have just upgraded this project for a guaranteed payment.

We are currently going through a re-branding exercise internally. Our logo is attached as a PDF file.

We are happy with our logo but would like to investigate how we can best apply the logo to our letterheads and compliment slips.

We are a quality printing company in England. Despite our name we are very professional and offer a personal service.

Our new website is under construction and here is a link to show you how it looks: http://tallowpress.marlwood.co.uk

The style must be professional and steer away from "tacky" otherwise it makes our company look very low budget and just a bit silly.

We would like to see elements of creativity though, so please, nothing too boring.

I have attached our new logo, there is an option for use on white or black.

Cheers
Tallowfern Team
Updates

Project Deadline Extended
Reason: We have increased the deadline due to an internal delay to things, we now have more time before we need anything to be printed.

Industry/Entity Type

Construction

Requirements
Must have
• IMPORTANT! Please do not tweak or change our logo in any way. A few designs show vast changes in the logo, this is not what we require. Please do not change the logo in any way. Thanks
Nice to have
• Classy but approachable. Elements of "quirky" would be nice to see.
Should not have
• A Tacky feel

```html
<!DOCTYPE html>
<html lang="en">
<head>
<meta charset="utf-8">
<title>Tallowfern Letterhead</title>
<link href="https://fonts.googleapis.com/css2?family=Montserrat:wght@700&family=Source+Sans+3:wght@400;600&family=Dancing+Script:wght@500&display=swap" rel="stylesheet">
<style>
  :root {
    --canvas: #e9e6e1;
    --paper: #ffffff;
    --ink: #1d1d1b;
    --body-ink: #5a5a5a;
    --pink: #e8217a;
    --white: #ffffff;
  }
  * { box-sizing: border-box; margin: 0; padding: 0; }
  html, body {
    width: 1200px;
    height: 1024px;
    overflow: hidden;
    background: var(--canvas);
  }
  .canvas {
    position: relative;
    width: 1200px;
    height: 1024px;
  }
  .letterhead {
    position: absolute;
    left: 260px;
    top: 32px;
    width: 680px;
    height: 960px;
    background: var(--paper);
    box-shadow: 0 4px 18px rgba(0,0,0,0.12);
    overflow: hidden;
  }
  .brand {
    position: absolute;
    top: 70px;
    left: 0;
    width: 100%;
    text-align: center;
  }
  .brand-name {
    display: inline-flex;
    align-items: center;
    gap: 10px;
    font-family: "Montserrat", sans-serif;
    font-weight: 700;
    font-size: 40px;
    letter-spacing: -0.5px;
    color: var(--ink);
  }
  .brand-dot {
    width: 16px;
    height: 16px;
    border-radius: 50%;
    background: var(--pink);
  }
  .brand-tagline {
    display: block;
    margin-top: 2px;
    padding-left: 120px;
    font-family: "Source Sans 3", sans-serif;
    font-weight: 600;
    font-size: 15px;
    color: var(--ink);
  }
  .letter {
    position: absolute;
    top: 190px;
    left: 66px;
    width: 548px;
    font-family: "Source Sans 3", sans-serif;
    color: var(--body-ink);
  }
  .salutation {
    font-size: 13px;
    margin-bottom: 14px;
  }
  .letter-body p {
    font-size: 10.5px;
    line-height: 1.38;
    text-align: justify;
    margin-bottom: 9px;
  }
  .sign-off {
    margin-top: 30px;
  }
  .signature {
    font-family: "Dancing Script", cursive;
    font-size: 22px;
    color: var(--body-ink);
  }
  .signer-role {
    font-size: 10.5px;
  }
  .footer-rule {
    position: absolute;
    left: 0;
    bottom: 118px;
    width: 680px;
    height: 3px;
    background: var(--ink);
  }
  .footer-band {
    position: absolute;
    left: 0;
    bottom: 0;
    width: 680px;
    height: 112px;
    background: var(--pink);
  }
  .contact-line {
    position: absolute;
    left: 60px;
    bottom: 26px;
    display: flex;
    align-items: center;
    gap: 16px;
    font-family: "Source Sans 3", sans-serif;
    font-size: 12.5px;
    color: var(--white);
  }
  .contact-item {
    display: inline-flex;
    align-items: center;
    gap: 5px;
  }
  .contact-icon {
    width: 12px;
    height: 12px;
  }
</style>
</head>
<body>
<div class="canvas">
  <article class="letterhead">
    <header class="brand">
      <div class="brand-name"><span class="brand-dot"></span>Tallowfern</div>
      <span class="brand-tagline">Quality Printing</span>
    </header>

    <section class="letter">
      <p class="salutation">Lorem Ipsum,</p>
      <div class="letter-body">
        <p>Duis sit amet dolor sit amet dolor tempor iaculis ac nec ante. Proin nunc diam, egestas eu semper a, fermentum ac leo. Fusce sit amet tempor elit. Mauris auctor interdum massa vitae cursus. Ut adipiscing pellentesque nunc eget tincidunt magna imperdiet non. Curabitur eleifend elementum nisi eget iaculis. Suspendisse scelerisque ligula a nunc faucibus sit amet elementum dolor dictum.</p>
        <p>Praesent condimentum mi at ultrices fermentum, ipsum lectus consequat mauris, ut vulputate nibh erat id eros. Vivamus ornare mattis libero at dictum. Praesent sodales metus sed nulla laoreet mollis. Curabitur non turpis in orci dignissim gravida. Aliquam tristique mauris a nibh vestibulum sagittis.</p>
        <p>Duis porta semper nibh, tincidunt aliquam metus euismod eget. Morbi varius varius pellentesque. Donec aliquam vulputate tortor non hendrerit. Suspendisse at ipsum ante, interdum porttitor ligula. Curabitur eu molestie sapien. Sed magna purus, faucibus quis pulvinar nec, commodo vel justo. Nam faucibus ornare varius. Vivamus sit amet felis vitae justo scelerisque malesuada. Etiam venenatis vehicula magna, at eleifend lorem ornare nec. Maecenas eu nisl vel nunc aliquet malesuada vel in lacus.</p>
        <p>Morbi et odio eu ante pharetra iaculis vitae eget arcu. Maecenas gravida, dui vel ultricies aliquet, dui arcu luctus ante, non dignissim ipsum tortor vel orci, ut fringilla mi. Mauris porta feugiat nibh et fermentum. Donec scelerisque consequat lacinia.</p>
        <p>Curabitur ac diam ut quam ultrices laoreet at ut tellus. Maecenas vitae urna in lorem condimentum sollicitudin eget vel lacus. Ut nisl turpis, tristique ullamcorper laoreet nec, gravida nec est. Donec elementum malesuada volutpat. In ac arcu quis augue vehicula fringilla.</p>
      </div>
      <div class="sign-off">
        <p class="signature">Yours Name</p>
        <p class="signer-role">Company Director</p>
      </div>
    </section>

    <div class="footer-rule" aria-hidden="true"></div>
    <div class="footer-band" aria-hidden="true"></div>

    <footer class="contact-line">
      <span class="contact-item">
        <svg class="contact-icon" viewBox="0 0 24 24" aria-hidden="true"><path fill="var(--white)" d="M6.6 10.8a15.1 15.1 0 0 0 6.6 6.6l2.2-2.2c.3-.3.7-.4 1-.2 1.1.4 2.3.6 3.6.6.6 0 1 .4 1 1V20c0 .6-.4 1-1 1A17 17 0 0 1 3 4c0-.6.4-1 1-1h3.5c.6 0 1 .4 1 1 0 1.3.2 2.5.6 3.6.1.3 0 .7-.2 1z"/></svg>
        0208 555 0174
      </span>
      <span class="contact-item">
        <svg class="contact-icon" viewBox="0 0 24 24" aria-hidden="true"><path fill="var(--white)" d="M2 5h20v14H2z"/><path fill="none" stroke="var(--pink)" stroke-width="2" d="M2 5l10 8 10-8"/></svg>
        orders@tallowfern.co.uk
      </span>
      <span class="contact-item">
        <svg class="contact-icon" viewBox="0 0 24 24" aria-hidden="true"><circle cx="12" cy="12" r="10" fill="none" stroke="var(--white)" stroke-width="2"/><path fill="none" stroke="var(--white)" stroke-width="1.6" d="M2 12h20M12 2c3 3 3 17 0 20M12 2c-3 3-3 17 0 20"/></svg>
        www.tallowpress.marlwood.co.uk
      </span>
    </footer>
  </article>
</div>
</body>
</html>
```